Larkmoor Business Allies Business Card

I'd Like a Two sided Card. Logo was uploaded as an EPS. If you need an additional type, let me know. Colors in Logo are Pantone 289C and Pantone 348C.

I'm thinking of raising the Print on the front, if that matters. Also would like any Vector Art used in the design included with the uploaded files when awarded. If you need any additional info, please let me know. Uploaded card design was for informational purposes only.

The back of the card should be blue, and I like the design included for the back.
Updates

On the Back of the Card, I will probably want my web address. (www.larkmoorbusinessallies.example)

Only Square Card Designs Please

Industry/Entity Type

Business

Requirements
Must have
• Should have enough room for longer email addresses in the future.
Nice to have
• email address above WEb URL.

```html
<!DOCTYPE html>
<html lang="en">
<head>
<meta charset="utf-8">
<title>Larkmoor Business Allies – Business Card</title>
<link rel="stylesheet" href="https://fonts.googleapis.com/css2?family=Open+Sans:wght@400;600;700&display=swap">
<style>
  :root {
    --navy: #0d2240;
    --green: #138a43;
    --white: #fafafa;
    --ink: #555a60;
    --backdrop: #e6e4e0;
  }
  html, body {
    margin: 0;
    width: 1200px;
    height: 1200px;
    overflow: hidden;
    background: var(--backdrop);
    font-family: "Open Sans", Arial, sans-serif;
  }
  .canvas {
    position: relative;
    width: 1200px;
    height: 1200px;
  }
  .card {
    position: absolute;
    left: 258px;
    width: 708px;
    height: 404px;
    background: var(--navy);
    box-shadow: 0 6px 18px rgba(0,0,0,0.25);
    overflow: hidden;
  }
  .card-front { top: 154px; }
  .card-back { top: 636px; }

  .front-shape {
    position: absolute;
    inset: 0;
  }

  .brand {
    position: absolute;
    display: flex;
    align-items: center;
    gap: 12px;
    font-weight: 700;
    text-transform: uppercase;
    letter-spacing: 1px;
  }
  .brand-mark {
    flex: none;
    display: block;
  }
  .brand-name { line-height: 1.05; }

  .front-brand {
    right: 24px;
    top: 22px;
    color: var(--navy);
    font-size: 27px;
  }
  .front-brand .brand-mark {
    width: 62px;
    height: 62px;
    background: var(--navy);
  }

  .person {
    position: absolute;
    left: 22px;
    top: 268px;
    width: 210px;
    text-align: right;
  }
  .person-name {
    margin: 0;
    color: var(--green);
    font-size: 31px;
    font-weight: 700;
    white-space: nowrap;
    text-align: left;
  }
  .person-title {
    margin: 2px 0 0;
    color: var(--ink);
    font-size: 20px;
    font-weight: 400;
  }

  .contact {
    position: absolute;
    left: 332px;
    top: 124px;
    color: var(--ink);
    font-size: 15px;
    line-height: 24px;
  }
  .contact-row {
    display: flex;
    align-items: flex-start;
    gap: 10px;
  }
  .contact-row svg {
    flex: none;
    width: 12px;
    height: 14px;
    margin-top: 5px;
    fill: var(--green);
  }
  .contact-gap { height: 14px; }

  .back-brand {
    left: 78px;
    top: 146px;
    color: var(--white);
    font-size: 44px;
  }
  .back-brand .brand-mark {
    width: 98px;
    height: 98px;
    background: var(--white);
    margin-right: 14px;
  }
  .back-web {
    position: absolute;
    left: 0;
    right: 0;
    top: 338px;
    text-align: center;
    color: var(--white);
    font-size: 19px;
  }
</style>
</head>
<body>
<main class="canvas">

  <section class="card card-front">
    <svg class="front-shape" viewBox="0 0 708 404" width="708" height="404" aria-hidden="true">
      <path d="M0,250 Q30,18 240,0 L708,0 L708,200 C690,330 440,378 0,360 Z" fill="var(--white)"/>
      <path d="M708,210 C690,342 440,388 0,368" fill="none" stroke="var(--green)" stroke-width="5"/>
    </svg>

    <div class="brand front-brand">
      <span class="brand-mark"></span>
      <span class="brand-name">Larkmoor<br>Business Allies</span>
    </div>

    <div class="contact">
      <div class="contact-row">
        <svg viewBox="0 0 12 14"><path d="M6 0a5 5 0 0 0-5 5c0 4 5 9 5 9s5-5 5-9a5 5 0 0 0-5-5zm0 7a2 2 0 1 1 0-4 2 2 0 0 1 0 4z"/></svg>
        <span>4120 Harbor Crest Lane<br>Fernwood Commons Plaza<br>Ashbury, VA 20100</span>
      </div>
      <div class="contact-gap"></div>
      <div class="contact-row">
        <svg viewBox="0 0 12 14"><path d="M1 5c0-2 2-3 5-3s5 1 5 3H8.5V4h-5v1zM2 6h8l1 6H1z"/></svg>
        <span>555.210.4830</span>
      </div>
      <div class="contact-row">
        <svg viewBox="0 0 12 14"><path d="M3 0h6a1 1 0 0 1 1 1v12a1 1 0 0 1-1 1H3a1 1 0 0 1-1-1V1a1 1 0 0 1 1-1zm0 2v9h6V2z"/></svg>
        <span>555.318.7264</span>
      </div>
      <div class="contact-row">
        <svg viewBox="0 0 12 14"><path d="M0 3h12v1L6 8 0 4zm0 2.5 6 4 6-4V11H0z"/></svg>
        <span>dwhitlow@larkmoorbusinessallies.example</span>
      </div>
    </div>

    <div class="person">
      <p class="person-name">R. Dana Whitlow</p>
      <p class="person-title">President</p>
    </div>
  </section>

  <section class="card card-back">
    <div class="brand back-brand">
      <span class="brand-mark"></span>
      <span class="brand-name">Larkmoor<br>Business Allies</span>
    </div>
    <p class="back-web">www.larkmoorbusinessallies.example</p>
  </section>

</main>
</body>
</html>
```